vestra charcoal

We need a package design for a 10 LBS/4.54kg of charcoal bag which will be printed on Kraft paper
the name of the product is Vestra Charcoal we will need a catchy logo for this
The design should have two colors red and any other. Please note that it will be printed on brown kraft paper. It should have our website on it www.vestracharcoal-example.com which should be obvious enough without congesting the design.
The design should not contravene any trademark.
It should feature the following qualities in a neat but catchy way:
100% all natural hardwood lump charcoal
No scrap, no fillers, burns hotter, cleaner and longer
No sparking, Low ash, top quality
Slogan:
...light the smoke flavor.
The design should make up just 40-50% of the paper space
It should have this warning info behind it or at the side
Warning
Carbon monoxide hazard
Burning charcoal inside homes or vehicles can kill you
It emits carbon monoxide which has no odor.
The following should be toked somewhere on the side
Manufactured by:
Kelvaro investment co. Ltd.
12, Tamburi Str. off elvoka Cross rd.
IkeJa lagos, Nigeria.
23419075521
2348159067714
info@vestracharcoal-example.com
Palvetta LLC USA
5027741963
palvet@vestracharcoal-example.com
The following information should be at the back
vestracharcoal is purely made from hardwood. It lights up fast and needs no petroleum starting fluid. It contains no chemicals or additive...just the purest form of charcoal.
Light up instruction: (please develop a diagrammatic representation for this)
1. Roll a full sheet of newspaper into a tube then form it into a donut shape.
2. Build the coals up around the donut shaped newspaper in a pyramid fashion.
3. light the paper in different places and let it go.
Other information will come in later

```html
<!DOCTYPE html>
<html lang="en">
<head>
<meta charset="utf-8">
<title>Vestra Charcoal – 10 lbs bag dieline</title>
<link rel="stylesheet" href="https://fonts.googleapis.com/css2?family=Arimo:wght@700&family=Pacifico&display=swap">
<style>
  :root {
    --kraft: #dfc8a0;
    --kraft-edge: #b9a37c;
    --ink: #231f20;
    --flame: #f4364a;
    --paper: #ffffff;
  }
  * { box-sizing: border-box; margin: 0; padding: 0; }
  html, body { width: 1200px; height: 875px; overflow: hidden; background: var(--paper); }
  .canvas { position: relative; width: 1200px; height: 875px; font-family: "Arimo", Arial, sans-serif; font-weight: 700; color: var(--ink); }
  .dieline { position: absolute; inset: 0; }
  .t { position: absolute; white-space: nowrap; }
  .script { font-family: "Pacifico", cursive; font-weight: 400; }

  /* front panel */
  .brand-mark { position: absolute; left: 44px; top: 196px; width: 52px; height: 52px; border-radius: 50%; background: var(--flame); }
  .brand-name { left: 112px; top: 206px; font-size: 28px; line-height: 32px; }
  .claim-lead { left: 33px; top: 418px; font-size: 31px; line-height: 40px; }
  .claim-main { left: 33px; top: 458px; font-size: 37px; line-height: 44px; }
  .claim-script { left: 33px; top: 550px; font-size: 31px; line-height: 44px; }
  .website { left: 104px; top: 757px; font-size: 22px; }
  .net-weight { left: 368px; top: 815px; font-size: 13px; }

  /* gusset */
  .warning { position: absolute; left: 533px; top: 752px; width: 108px; height: 54px; padding: 4px;
    background: repeating-linear-gradient(45deg, var(--flame) 0 4px, var(--paper) 4px 8px); }
  .warning-inner { width: 100%; height: 100%; background: var(--kraft); border: 1px solid var(--ink); text-align: center; padding-top: 2px; }
  .warning-title { font-size: 7px; font-weight: 400; font-family: Arial, sans-serif; }
  .warning-copy { font-size: 4.6px; line-height: 5.4px; padding: 1px 4px 0; white-space: normal; }

  /* back panel */
  .qualities { left: 880px; top: 58px; font-size: 19px; line-height: 25px; }
  .instr-title { left: 822px; top: 165px; font-size: 21px; }
  .step-no { font-size: 11px; }
  .step-copy { font-size: 12px; line-height: 14px; }
  .step-art { position: absolute; border-radius: 6px; background: linear-gradient(180deg, #6b5d4a, var(--ink)); opacity: .85; }
  .about { left: 700px; top: 535px; width: 460px; text-align: center; font-size: 12.5px; line-height: 16px; }
  .about-script { left: 700px; top: 590px; width: 460px; text-align: center; font-size: 17px; }
  .maker { left: 700px; top: 652px; width: 450px; text-align: center; font-size: 12.5px; line-height: 15px; }
  .partner { left: 700px; top: 772px; width: 450px; text-align: center; font-size: 12.5px; line-height: 15px; }
</style>
</head>
<body>
<div class="canvas">
  <svg class="dieline" width="1200" height="875" viewBox="0 0 1200 875" aria-hidden="true">
    <g fill="var(--kraft)" stroke="var(--kraft-edge)" stroke-width="1">
      <rect x="22" y="2" width="475" height="11"/>
      <polygon points="25,13 478,13 490,855 22,855"/>
      <polygon points="566,10 608,10 665,848 510,848"/>
      <rect x="678" y="5" width="490" height="12"/>
      <polygon points="700,17 1150,17 1160,852 686,852"/>
    </g>
    <line x1="587" y1="24" x2="587" y2="740" stroke="var(--ink)" stroke-width="2"/>
  </svg>

  <!-- front -->
  <div class="brand-mark"></div>
  <div class="t brand-name">VESTRA CHARCOAL</div>
  <div class="t claim-lead">100%</div>
  <div class="t claim-main">ALL NATURAL<br>CHARCOAL</div>
  <div class="t script claim-script">No scrap<br>No fillers<br>Burns hotter,<br>Cleaner and Longer</div>
  <div class="t website">www.vestracharcoal-example.com</div>
  <div class="t net-weight">10 LBS/4.54kg</div>

  <!-- gusset -->
  <div class="warning">
    <div class="warning-inner">
      <div class="warning-title">WARNING</div>
      <div class="warning-copy">Carbon monoxide hazard. Burning charcoal inside homes or vehicles can kill you. It emits carbon monoxide which has no odor.</div>
    </div>
  </div>

  <!-- back -->
  <div class="t qualities">NO SPARKING,<br>LOW ASH,<br>TOP QUALITY.</div>
  <div class="t script instr-title">Light up instruction:</div>

  <div class="t step-no" style="left:706px;top:256px">1.</div>
  <div class="step-art" role="img" aria-label="Newspaper rolled into a tube and shaped into a donut" style="left:737px;top:238px;width:66px;height:42px"></div>
  <div class="t step-copy" style="left:838px;top:248px">ROLL A FULL SHEET OF NEWSPAPER INTO A<br>TUBE, THEN FORM IT INTO A DONUT SHAPE.</div>

  <div class="t step-no" style="left:706px;top:342px">2.</div>
  <div class="step-art" role="img" aria-label="Coals stacked in a pyramid on a grill around the newspaper" style="left:733px;top:322px;width:74px;height:50px"></div>
  <div class="t step-copy" style="left:838px;top:333px">BUILD THE COALS UP AROUND THE DONUT<br>SHAPED NEWSPAPER IN A PYRAMID FASHION.</div>

  <div class="t step-no" style="left:706px;top:448px">3.</div>
  <div class="step-art" role="img" aria-label="Lit coals on a grill with red flames rising" style="left:733px;top:385px;width:78px;height:88px;background:linear-gradient(180deg,var(--flame) 0 45%,var(--ink) 70%)"></div>
  <div class="t step-copy" style="left:838px;top:440px">LIGHT THE PAPER IN DIFFERENT PLACES<br>AND LET IT GO...</div>

  <div class="t about">VESTRA CHARCOAL IS PURELY MADE FROM HARDWOOD. IT<br>LIGHTS UP FAST AND NEEDS NO PETROLEUM STARTING<br>FLUID. IT CONTAINS NO CHEMICALS OR ADDITIVES</div>
  <div class="t script about-script">. . . just the purest form of charcoal.</div>
  <div class="t maker">MANUFACTURED BY:<br>KELVARO INVESTMENT CO. LTD.<br>12, TAMBURI STR. OFF ELVOKA CROSS RD.<br>IKEJA LAGOS, NIGERIA.<br>23419075521<br>2348159067714<br>INFO@VESTRACHARCOAL-EXAMPLE.COM</div>
  <div class="t partner">PALVETTA LLC USA<br>5027741963<br>PALVET@VESTRACHARCOAL-EXAMPLE.COM</div>
</div>
</body>
</html>
```